Create a Magazine Ad for an asbestos law firm

we need an 8 X 13 ad to be on the back of a magazine cover. We have the text Attached and want a similar look and feel to our website : www.harborvale-claims.example. The ad should be targeted to white males 55 years or older who are conservative and worked in industry or industrial plants. The main offer is a free case review and trying to get them to call the telephone number.

Target Market(s)

White collar men who worked in industrial plants. Age 55 years or older.

Industry/Entity Type

Legal

Requirements
Must have
• Pictures of white middle class conservative man or man and woman
Nice to have
• look at www.harborvale-claims.example to an. idea of what we are looking for

```html
<!DOCTYPE html>
<html lang="en">
<head>
<meta charset="utf-8">
<title>Diagnosed with Mesothelioma – Free Case Evaluation</title>
<link href="https://fonts.googleapis.com/css2?family=Arimo:wght@400;700&family=Oswald:wght@500&display=swap" rel="stylesheet">
<style>
  :root {
    --teal: #1b687c;
    --teal-deep: #13505f;
    --gold: #f9b918;
    --white: #ffffff;
    --photo-top: #d7b49c;
    --photo-mid: #dfa93c;
    --photo-low: #c3d2e3;
  }
  * { margin: 0; padding: 0; box-sizing: border-box; }
  html, body { width: 738px; height: 1200px; overflow: hidden; background: var(--teal); }
  .ad {
    position: relative; width: 738px; height: 1200px; overflow: hidden;
    background: var(--teal); color: var(--white);
    font-family: "Oswald", "Arial Narrow", sans-serif; font-weight: 500;
  }
  .frame {
    position: absolute; left: 25px; top: 36px; width: 689px; height: 1100px;
    border: 5px solid var(--white); border-bottom: none;
  }
  .portrait {
    position: absolute; left: 172px; top: 28px; width: 450px; height: 366px;
    border-radius: 14px 14px 0 0;
    background: linear-gradient(180deg, var(--photo-top) 0%, var(--photo-mid) 62%, var(--photo-low) 100%);
  }
  .headline-band-outline {
    position: absolute; left: -4px; top: 408px; width: 724px; height: 149px;
    border: 3px solid var(--gold);
  }
  .headline-band {
    position: absolute; left: 0; top: 393px; width: 707px; height: 147px;
    background: var(--gold); border-radius: 0 3px 3px 0;
    box-shadow: 3px 4px 6px rgba(0,0,0,.35);
    font-family: "Arimo", Arial, sans-serif; font-weight: 700; text-align: center;
  }
  .headline-kicker {
    position: absolute; left: 0; right: 0; top: 8px;
    font-size: 52px; line-height: 1; color: var(--white); padding-left: 42px;
  }
  .headline-main {
    position: absolute; left: 0; right: 0; top: 58px;
    font-size: 76px; line-height: 1; color: var(--teal); letter-spacing: -0.5px; padding-left: 40px;
  }
  .section-title {
    position: absolute; left: 0; width: 738px; top: 583px; text-align: center;
    font-family: "Arimo", Arial, sans-serif; font-weight: 700; font-size: 25px; letter-spacing: .3px;
  }
  .copy { position: absolute; white-space: nowrap; }
  .copy-left, .copy-right { top: 614px; font-size: 15.5px; line-height: 18.5px; }
  .copy-left { left: 46px; }
  .copy-right { left: 386px; }
  .bullets { position: absolute; list-style: none; font-size: 12.3px; line-height: 15.4px; white-space: nowrap; }
  .bullets li::before { content: "•"; margin-right: 5px; }
  .bullets-left { left: 44px; top: 689px; }
  .bullets-right { left: 382px; top: 670px; }
  .subhead {
    position: absolute; left: 46px; font-family: "Arimo", Arial, sans-serif; font-weight: 700;
    color: var(--gold); line-height: 1; white-space: nowrap;
  }
  .subhead-trust { top: 753px; font-size: 17px; }
  .subhead-money { top: 852px; font-size: 15.5px; }
  .copy-wide { left: 46px; font-size: 14.3px; line-height: 16px; }
  .copy-trust { top: 786px; }
  .copy-money { top: 884px; }
  .settlements {
    position: absolute; left: 46px; top: 947px; width: 660px;
    display: grid; grid-template-columns: 360px 300px; row-gap: 16px;
    font-family: "Arimo", Arial, sans-serif;
  }
  .settlement-amount { display: block; color: var(--gold); font-weight: 700; font-size: 19px; line-height: 22px; }
  .settlement-source { display: block; font-size: 15px; line-height: 18px; letter-spacing: -.7px; white-space: nowrap; }
  .call-bar {
    position: absolute; left: 0; top: 1126px; width: 738px; height: 46px;
    background: var(--gold); color: var(--teal); text-align: center; white-space: nowrap;
    font-size: 13.6px; line-height: 17px; padding-top: 5px; letter-spacing: -.2px;
  }
  .footer-shade {
    position: absolute; left: 0; top: 1172px; width: 738px; height: 28px;
    background: linear-gradient(var(--teal-deep), var(--teal) 90%);
  }
</style>
</head>
<body>
<main class="ad">
  <div class="frame"></div>
  <div class="portrait" role="img" aria-label="Photo of a smiling older man in a light blue shirt with a mustard sweater over his shoulders, pointing at the viewer"></div>

  <div class="headline-band-outline"></div>
  <header class="headline-band">
    <div class="headline-kicker">DIAGNOSED WITH</div>
    <h1 class="headline-main">MESOTHELIOMA</h1>
  </header>

  <h2 class="section-title">YOU COULD BE OWED COMPENSATION</h2>

  <p class="copy copy-left">It's very likely you developed this disease through<br>asbestos exposure. Mesothelioma patients are getting<br>multi-million dollar settlements, decades later, from:</p>
  <ul class="bullets bullets-left">
    <li>Exposure to asbestos products,</li>
    <li>Ex-employers, or</li>
    <li>Talcum baby powder companies.</li>
  </ul>

  <p class="copy copy-right">We can help you find out if you qualify for a case in<br>minutes.</p>
  <ul class="bullets bullets-right">
    <li>We'll analyze your situation at no cost</li>
    <li>Determine how much compensation you could be entitled too</li>
    <li>Show you the next steps to get what you're owed</li>
  </ul>

  <h3 class="subhead subhead-trust">$30 BILLION IS AVAILABLE IN TRUST FOR MESOTHELIOMA PATIENTS</h3>
  <p class="copy copy-wide copy-trust">Tradesmen in many industries were negligently exposed to asbestos materials well into the 1990s. Whether you<br>developed Mesothelioma yourself due to asbestos exposure or you're the surviving family of a lost loved one you could<br>be entitled to significant compensation.</p>

  <h3 class="subhead subhead-money">HOW MUCH MONEY CAN PEOPLE RECEIVE FROM A MESOTHELIOMA CASE?</h3>
  <p class="copy copy-wide copy-money">Depending on where you were exposed and a few other factors, you can get a settlement from 6 to 7 figures. Here are<br>a few examples of Mesothelioma Settlements received by our clients. These figures are the total compensation after all<br>attorney fees and expenses are deducted.</p>

  <div class="settlements">
    <div><span class="settlement-amount">$6,142,500</span><span class="settlement-source">Exposed through heavy duty vehicles</span></div>
    <div><span class="settlement-amount">$3,921,750</span><span class="settlement-source">Exposed through navy service</span></div>
    <div><span class="settlement-amount">$6,033,510</span><span class="settlement-source">Exposed through general contracting</span></div>
    <div><span class="settlement-amount">$3,600,450</span><span class="settlement-source">Exposed through navy service</span></div>
    <div><span class="settlement-amount">$5,939,010</span><span class="settlement-source">Exposed through boat repair</span></div>
    <div><span class="settlement-amount">$2.5 MILLION</span><span class="settlement-source">Exposed from Brand-Name Talcum Baby Powder.</span></div>
  </div>

  <footer class="call-bar">
    Find out if you're Eligible, for FREE, in Minutes. We'll evaluate your situation and tell you what your case could be worth. Get your<br>
    Free evaluation now! CALL 1-XXX XXXX (good number)&nbsp; Marlow &amp; Pryce, LLP, Owen Marlow, Bayport, TX
  </footer>
  <div class="footer-shade"></div>
</main>
</body>
</html>
```